Landing Page für Persönlichkeitsquiz
Zielgruppe
Persönlichkeitsquiz für Menschen über 40 Jahren die bessere Entscheidungen treffen möchten.
Aufgabenstellung
Landinpage Design plus QUIZ ( 6 Schritte)
Vollständige Projektbeschreibung:
Projektbeschreibung
„Roaming Sideways QUIZ“
roamingsideways.example
- Responsive Design für mobile & website (Most users: mobile)
- Design wird Grundlage für spätere Website
Dieses Quiz wendet sich an Menschen über 40 Jahre, die ihre persönlichen Lebensziele besser erreichen möchten. Bitte denke daran, dass Menschen in unserem Alter schon schlechter sehen – also bitte eine gut lesbare & etwas größere Schrift verwenden!
Auftrag:
QUIZ mit mehreren Runden
Schritte des Quiz:
1. Landingpage
1.1 Video (youtube eingebunden)
1.2 Text
1.3 „Start Quiz“ Button
1.4 „Bekannt aus“ mit Logos von Medien in denen Marv Olden besprochen wurde.
1.5 Testimonials?
QUIZ (Popup)
2. Erste Runde: „Kille“ alle Antworten die Dich nicht interessieren. Total 64 Antworten.
2.1 Text mit Aufgabenbeschreibung „Kille“ alle Antworten die Dich nicht interessieren. Du hast zwei Minuten.“
2.2 Ein Button pro Antwort (wie bei Lernivo)
2.3 Zwei Buttons pro Reihe
2.4 Oben: Progress bar
2.5 Oben: Countdown clock, Restzeit: 2 Minuten
3. Zweite Runde: „Wähle max. 18 Antworten aus die überleben sollen.“
3.1 Text mit Aufgabenbeschreibung „Wähle max. 18 Antworten aus die überleben sollen.“
3.2 Ein Button pro Antwort (wie bei Lernivo)
3.3 Zwei Buttons pro Reihe
3.4 Oben: Progress bar
3.5 Oben: Countdown clock, Restzeit: 60 Sekunden
3.6 Zähler der noch verfügbaren Antworten. Hier: Noch 18, noch 17, noch 16.. etc.
4. Dritte Runde: „Nur 9 Antworten dürfen überleben. Go!“
4.1 Text mit „Nur 9 Antworten dürfen überleben. Go!“
4.2 Ein Button pro Antwort (wie bei Lernivo)
4.3 Zwei Buttons pro Reihe
4.4 Oben: Progress bar
4.5 Oben: Countdown clock, Restzeit 45 ..

```html
<!DOCTYPE html>
<html lang="de">
<head>
<meta charset="utf-8">
<title>Roaming Sideways Quiz</title>
<link href="https://fonts.googleapis.com/css2?family=Open+Sans:wght@400;600;700&display=swap" rel="stylesheet">
<style>
:root{
  --hero-a:#3e1590;
  --hero-b:#2a0e84;
  --band:#633db5;
  --reviews:#5c37ad;
  --card:#6940bf;
  --card-edge:#4c2694;
  --footer:#34128c;
  --ink-dim:#1f0d4f;
  --ink-soft:#5d3aa8;
  --accent:#c46bd6;
  --gold:#e0a82e;
  --grey-bg:#ececec;
  --grey-text:#6f6f6f;
  --cta-dim:#6a2b55;
  --cta-text:#9b55d4;
  --white:#ffffff;
}
*{box-sizing:border-box;margin:0;padding:0}
html,body{width:1161px;height:1200px;overflow:hidden}
body{font-family:"Open Sans",sans-serif;background:var(--reviews);position:relative}
.hero{position:absolute;left:0;top:0;width:1161px;height:550px;background:linear-gradient(100deg,var(--hero-a),var(--hero-b));overflow:hidden}
.brand{position:absolute;left:85px;top:52px;font-weight:700;font-size:17px;line-height:23px;color:var(--ink-soft);letter-spacing:.3px}
.nav{position:absolute;top:80px;right:86px;display:flex;gap:30px;font-size:13.5px;color:var(--ink-soft)}
.nav .lang::after{content:"";display:inline-block;width:6px;height:6px;border-right:1.5px solid var(--ink-soft);border-bottom:1.5px solid var(--ink-soft);transform:rotate(45deg);margin-left:9px;position:relative;top:-3px}
.hero-title{position:absolute;left:85px;top:192px;font-size:24px;line-height:34px;font-weight:700;color:var(--ink-soft)}
.hero-text{position:absolute;left:85px;top:276px;font-size:12px;line-height:17px;color:var(--ink-soft);white-space:nowrap}
.hero-cta{position:absolute;left:85px;top:350px;width:130px;height:36px;border-radius:18px;background:var(--cta-dim);color:var(--cta-text);font-weight:700;font-size:13px;display:flex;align-items:center;padding-left:14px;gap:6px}
.video{position:absolute;left:960px;top:144px;width:115px;height:270px;background:linear-gradient(160deg,#5d2298,#4e1a8c)}
.video-knob{position:absolute;left:980px;top:116px;width:38px;height:38px;border-radius:50%;background:#5a1fa0}
.modal{position:absolute;left:168px;top:112px;width:824px;height:416px;background:var(--white);border-bottom:4px solid var(--accent);box-shadow:0 6px 20px rgba(20,0,60,.35)}
.step{position:absolute;left:395px;top:-18px;width:36px;height:36px;border-radius:50%;background:var(--accent);border:2px solid var(--white);color:var(--white);font-weight:700;font-size:17px;display:flex;align-items:center;justify-content:center}
.topbar{position:absolute;left:30px;right:30px;top:22px;height:20px;font-size:15px;display:flex;align-items:center}
.back{color:var(--gold);font-weight:700;display:flex;align-items:center;gap:7px}
.timer{position:absolute;left:273px;display:flex;align-items:center;gap:7px;color:var(--accent);font-weight:700}
.rest{position:absolute;left:360px;color:var(--grey-text);padding-left:8px;border-left:1px solid #ddd}
.done{position:absolute;right:0;color:var(--accent);font-weight:700}
.progress{position:absolute;left:30px;top:58px;width:764px;height:11px;border-radius:6px;background:var(--grey-bg)}
.progress span{display:block;width:188px;height:11px;border-radius:6px;background:var(--accent)}
.task{position:absolute;left:0;right:0;top:91px;text-align:center;font-size:21px;font-weight:700;color:var(--grey-text)}
.task-sub{position:absolute;left:0;right:0;top:120px;text-align:center;font-size:14px;color:var(--grey-text)}
.answers{position:absolute;left:167px;top:162px;width:491px;display:grid;grid-template-columns:240px 241px;column-gap:10px;row-gap:9px}
.answer{height:47px;background:var(--grey-bg);color:var(--grey-text);font-size:13.5px;display:flex;align-items:center;justify-content:space-between;padding:0 16px 0 10px;white-space:nowrap}
.answer .box{flex:none;width:15px;height:15px;background:var(--white);display:flex;align-items:center;justify-content:center}
.answer.is-picked{background:var(--accent);color:var(--white)}
.scroll{position:absolute;left:686px;top:146px;width:7px;height:243px;border-radius:4px;background:var(--grey-bg)}
.scroll span{position:absolute;top:11px;left:0;width:7px;height:49px;border-radius:4px;background:var(--accent)}
.next{position:absolute;right:30px;top:360px;color:var(--gold);font-weight:700;font-size:15px;display:flex;align-items:center;gap:7px}
.press{position:absolute;left:0;top:550px;width:1161px;height:254px;background:var(--band)}
.section-title{position:absolute;left:0;right:0;text-align:center;font-weight:700;font-size:15px;color:var(--ink-dim)}
.section-title::after{content:"";display:block;width:39px;height:3px;background:#4a2398;margin:8px auto 0}
.press .section-title{top:38px}
.outlets{position:absolute;left:122px;top:108px;width:920px;height:75px;display:flex;align-items:center;justify-content:space-between}
.outlet{font-weight:700;font-size:20px;color:var(--ink-dim)}
.arrow{position:absolute;top:137px;width:18px;height:18px;border-radius:50%;background:var(--cta-dim);display:flex;align-items:center;justify-content:center}
.deco-right{position:absolute;left:1118px;top:581px;width:170px;height:170px;border-radius:50%;background:#3b1690}
.deco-left{position:absolute;left:-130px;top:851px;width:176px;height:183px;border-radius:50%;background:#3a1590}
.reviews .section-title{top:848px}
.card{position:absolute;top:912px;width:324px;height:152px;background:var(--card);border-bottom:3px solid var(--card-edge)}
.avatar{position:absolute;left:16px;top:17px;width:66px;height:66px;border-radius:50%;background:linear-gradient(140deg,#4a2c6e,#2c1a48)}
.name{position:absolute;left:99px;top:32px;font-weight:700;font-size:13.5px;color:var(--ink-dim)}
.from{position:absolute;left:99px;top:54px;font-size:10px;color:var(--ink-dim)}
.from b{font-weight:700;margin-left:4px}
.quote{position:absolute;left:16px;top:98px;right:16px;font-size:10.5px;line-height:14.5px;color:var(--ink-dim)}
.bubble{position:absolute;right:14px;top:12px}
.cta{position:absolute;left:518px;top:1093px;width:125px;height:36px;border-radius:18px;background:var(--cta-dim);color:var(--cta-text);font-weight:700;font-size:13px;display:flex;align-items:center;justify-content:center;gap:6px}
.footer{position:absolute;left:0;top:1155px;width:1161px;height:45px;background:var(--footer);font-size:11px;color:#4a26a0}
.footer .copy{position:absolute;left:85px;top:15px}
.footer .links{position:absolute;right:87px;top:15px;display:flex;gap:32px}
</style>
</head>
<body>

<header class="hero">
  <div class="brand">ROAMING<br>SIDEWAYS</div>
  <nav class="nav"><span class="lang">Deutsch</span><span>Fragen</span></nav>
  <h1 class="hero-title">Herzlich willkommen<br>bei Roaming Sideways</h1>
  <p class="hero-text">Lorem ipsum dolor sit amet, consetetur sadipscing elitr, sed diam<br>nonumy eirmod tempor invidunt ut labore et dolore magna<br>aliquyam erat, sed diam voluptua.</p>
  <div class="hero-cta"><svg width="12" height="12" viewBox="0 0 12 12"><path d="M1 6h9M6 2l4 4-4 4" stroke="currentColor" stroke-width="1.6" fill="none"/></svg>Quiz starten</div>
  <div class="video-knob"></div>
  <div class="video" role="img" aria-label="Eingebundenes Einführungsvideo"></div>
</header>

<section class="modal" aria-label="Quiz Runde 1">
  <div class="step">1</div>
  <div class="topbar">
    <span class="back"><svg width="18" height="18" viewBox="0 0 18 18"><circle cx="9" cy="9" r="9" fill="currentColor"/><path d="M10.5 5l-4 4 4 4" stroke="#fff" stroke-width="1.8" fill="none"/></svg>zurück</span>
    <span class="timer"><svg width="17" height="17" viewBox="0 0 17 17"><circle cx="8.5" cy="8.5" r="7.5" stroke="currentColor" stroke-width="1.6" fill="none"/><path d="M8.5 4v5h3.5" stroke="currentColor" stroke-width="1.6" fill="none"/></svg>02 : 00</span>
    <span class="rest">Restzeit: 2 Minuten</span>
    <span class="done">0 % komplett</span>
  </div>
  <div class="progress"><span></span></div>
  <h2 class="task">„Kille“ alle Antworten die Dich nicht interessieren.</h2>
  <p class="task-sub">Du hast zwei Minuten.</p>
  <div class="answers">
    <div class="answer is-picked">Lorem ipsum dela martime de.<span class="box"><svg width="12" height="10" viewBox="0 0 12 10"><path d="M1 5l3.5 3.5L11 1" stroke="#c46bd6" stroke-width="2" fill="none"/></svg></span></div>
    <div class="answer">Lorem ipsum dela martime de.<span class="box"></span></div>
    <div class="answer">Lorem ipsum dela martime de.<span class="box"></span></div>
    <div class="answer">Lorem ipsum dela martime de.<span class="box"></span></div>
    <div class="answer">Lorem ipsum dela martime de.<span class="box"></span></div>
    <div class="answer is-picked">Lorem ipsum dela martime de.<span class="box"><svg width="12" height="10" viewBox="0 0 12 10"><path d="M1 5l3.5 3.5L11 1" stroke="#c46bd6" stroke-width="2" fill="none"/></svg></span></div>
    <div class="answer">Lorem ipsum dela martime de.<span class="box"></span></div>
    <div class="answer">Lorem ipsum dela martime de.<span class="box"></span></div>
  </div>
  <div class="scroll"><span></span></div>
  <div class="next">weiter<svg width="18" height="18" viewBox="0 0 18 18"><circle cx="9" cy="9" r="9" fill="currentColor"/><path d="M7.5 5l4 4-4 4" stroke="#fff" stroke-width="1.8" fill="none"/></svg></div>
</section>

<section class="press">
  <h2 class="section-title">Bekannt aus</h2>
  <div class="arrow" style="left:84px"><svg width="8" height="10" viewBox="0 0 8 10"><path d="M6 1L2 5l4 4" stroke="#9b55d4" stroke-width="1.6" fill="none"/></svg></div>
  <div class="outlets">
    <span class="outlet">Kanal Neun</span>
    <span class="outlet">Tagesblick</span>
    <span class="outlet">Nordfunk</span>
    <span class="outlet">Europaweit</span>
    <span class="outlet">Stadtwelle</span>
    <span class="outlet">Westklang</span>
    <span class="outlet">Infokanal</span>
  </div>
  <div class="arrow" style="left:1059px"><svg width="8" height="10" viewBox="0 0 8 10"><path d="M2 1l4 4-4 4" stroke="#9b55d4" stroke-width="1.6" fill="none"/></svg></div>
</section>
<div class="deco-right"></div>

<section class="reviews">
  <div class="deco-left"></div>
  <h2 class="section-title">Was sagen andere zum Quiz</h2>
  <article class="card" style="left:85px">
    <div class="avatar" role="img" aria-label="Porträtfoto von Fatima Mustermann"></div>
    <svg class="bubble" width="20" height="20" viewBox="0 0 20 20"><path d="M10 2a8 7.5 0 1 1-4.5 13.7L2 17l1.2-3.6A8 7.5 0 0 1 10 2z" stroke="#4a2398" stroke-width="1.5" fill="none"/></svg>
    <div class="name">Fatima Mustermann</div>
    <div class="from">aus<b>Berlin</b></div>
    <p class="quote">Lorem ipsum dolor sit amet, consetetur sadipscing elitr, sed diam nonumy eirmod tempor invidunt ut labore et dolore magna aliquyam erat, sed diam voluptua.</p>
  </article>
  <article class="card" style="left:418px">
    <div class="avatar" role="img" aria-label="Porträtfoto von James Mustermelian"></div>
    <svg class="bubble" width="20" height="20" viewBox="0 0 20 20"><path d="M10 2a8 7.5 0 1 1-4.5 13.7L2 17l1.2-3.6A8 7.5 0 0 1 10 2z" stroke="#4a2398" stroke-width="1.5" fill="none"/></svg>
    <div class="name">James Mustermelian</div>
    <div class="from">aus<b>Bayern</b></div>
    <p class="quote">Lorem ipsum dolor sit amet, consetetur sadipscing elitr, sed diam nonumy eirmod tempor invidunt ut labore et dolore magna aliquyam erat, sed diam voluptua.</p>
  </article>
  <article class="card" style="left:752px">
    <div class="avatar" role="img" aria-label="Porträtfoto von Christiane Weißfuss"></div>
    <svg class="bubble" width="20" height="20" viewBox="0 0 20 20"><path d="M10 2a8 7.5 0 1 1-4.5 13.7L2 17l1.2-3.6A8 7.5 0 0 1 10 2z" stroke="#4a2398" stroke-width="1.5" fill="none"/></svg>
    <div class="name">Christiane Weißfuss</div>
    <div class="from">aus<b>Hannover</b></div>
    <p class="quote">Lorem ipsum dolor sit amet, consetetur sadipscing elitr, sed diam nonumy eirmod tempor invidunt ut labore et dolore magna aliquyam erat, sed diam voluptua.</p>
  </article>
  <div class="cta"><svg width="12" height="12" viewBox="0 0 12 12"><path d="M1 6h9M6 2l4 4-4 4" stroke="currentColor" stroke-width="1.6" fill="none"/></svg>Quiz starten</div>
</section>

<footer class="footer">
  <span class="copy">© Roaming Sideways QUIZ</span>
  <span class="links"><span>Impressum</span><span>Datenschutz</span><span>Sitemap</span></span>
</footer>

</body>
</html>
```